Business Card Design for BrightlaneReach.com

--I need a business card design for my company BrightlaneReach.com

I have attached my logo...I want the brightlane reach logo on the front of the business card, and then I want The Brightlane Chief on the back of it with my information.

I would like to see a light colored background as well as a dark colored background

FRONT:
BRIGHTLANE REACH LOGO
247 E. Pelham Row
5th Floor
San Diego CA 92384
www.BrightlaneReach.com

Advanced Website & App Development
Websites, Apps, Online Voucher Systems

Leading Edge Marketing Services
SMS, VB, SMM, SEM,

BACK:
BRIGHTLANE CHIEF LOGO
Dorian Welker
The Brightlane Chief
Call Or Text: 555-204-3378
Dorian@BrightlaneChief.com
www.BrightlaneChief.com

Target Market(s)

small business owners

Industry/Entity Type

Business Consultant

Contact Information for Business Card

FRONT:
BRIGHTLANE REACH LOGO
247 E. Pelham Row
5th Floor
San Diego CA 92384
www.BrightlaneReach.com

SMS, VB, SMM, SEM,

BACK:
BRIGHTLANE CHIEF LOGO
Dorian Welker
The Brightlane Chief
Dorian@BrightlaneChief.com
www.BrightlaneChief.com

Requirements
Must have
• add this quote on it somewhere, anywhere,preferrably on back
• "The Fastest Way To Success Is To Take Action”
• — Dorian Welker, Brightlane Chief
Nice to have
• open
Should not have
• red

```html
<!DOCTYPE html>
<html lang="en">
<head>
<meta charset="utf-8">
<title>Brightlane Reach — Business Cards</title>
<link rel="stylesheet" href="https://fonts.googleapis.com/css2?family=Source+Sans+3:wght@400;600;700&display=swap">
<style>
  :root {
    --backdrop: #454545;
    --brand-blue: #0b72ac;
    --card-white: #ffffff;
    --ink-white: #ffffff;
    --ink-grey: #6d6e70;
  }
  * { box-sizing: border-box; margin: 0; padding: 0; }
  html, body {
    width: 1105px;
    height: 1200px;
    overflow: hidden;
    background: var(--backdrop);
    font-family: "Source Sans 3", "Myriad Pro", sans-serif;
  }
  .canvas { position: relative; width: 1105px; height: 1200px; }

  .card {
    position: absolute;
    left: 196px;
    width: 720px;
    height: 411px;
    text-align: center;
  }

  /* Front */
  .card--front {
    top: 146px;
    background: var(--brand-blue);
    color: var(--ink-white);
  }
  .front__name {
    position: absolute;
    top: 86px;
    left: 0; right: 0;
    font-size: 40px;
    font-weight: 400;
    letter-spacing: 4px;
    line-height: 1;
  }
  .front__details {
    position: absolute;
    top: 170px;
    left: 0; right: 0;
    font-size: 20px;
    line-height: 26px;
  }
  .front__details p { margin: 0; }
  .front__details .web { font-weight: 700; }
  .front__details .group { margin-top: 14px; }

  /* Back */
  .card--back {
    top: 602px;
    background: var(--card-white);
  }
  .back__name {
    position: absolute;
    top: 90px;
    left: 0; right: 0;
    font-size: 42px;
    font-weight: 600;
    letter-spacing: 4px;
    color: var(--brand-blue);
    line-height: 1;
  }
  .back__band {
    position: absolute;
    left: 0; right: 0;
    top: 236px;
    height: 142px;
    background: var(--brand-blue);
    color: var(--ink-white);
    padding-top: 24px;
    font-size: 20px;
    line-height: 29px;
  }
  .back__band .person {
    font-size: 26px;
    font-weight: 600;
    line-height: 34px;
  }
  .back__band .person .divider { font-weight: 400; margin: 0 4px; }
  .back__band .person .role { font-size: 20px; font-weight: 400; }
  .back__band b { font-weight: 700; }
  .back__quote {
    position: absolute;
    left: 0; right: 0;
    top: 378px;
    height: 33px;
    line-height: 33px;
    font-size: 15px;
    color: var(--ink-grey);
    white-space: nowrap;
  }
</style>
</head>
<body>
<main class="canvas">

  <section class="card card--front" aria-label="Card front">
    <div class="front__name">BRIGHTLANE REACH</div>
    <div class="front__details">
      <p>247 E. Pelham Row, 5th Floor, San Diego CA 92384</p>
      <p class="web">www.BrightlaneReach.com</p>
      <div class="group">
        <p>Advanced Website &amp; App Development</p>
        <p>Websites • Apps • Online Voucher Systems</p>
      </div>
      <div class="group">
        <p>Leading Edge Marketing Services</p>
        <p>SMS • VB • SMM • SEM</p>
      </div>
    </div>
  </section>

  <section class="card card--back" aria-label="Card back">
    <div class="back__name">BRIGHTLANE CHIEF</div>
    <div class="back__band">
      <p class="person">Dorian Welker<span class="divider">|</span><span class="role">The Brightlane Chief</span></p>
      <p><b>Phone:</b> 555-204-3378&nbsp; <b>Email:</b> Dorian@BrightlaneChief.com</p>
      <p><b>Web:</b> www.BrightlaneChief.com</p>
    </div>
    <p class="back__quote">“The Fastest Way To Success Is To Take Action” — Dorian Welker, Brightlane Chief</p>
  </section>

</main>
</body>
</html>
```